I need to make a car magnet

It needs to include the words "KLAVO TOUR" and "2026 MEMBER" as well as the attached silhouette of the golfer. The color scheme needs to be navy, red and white. The shape and dimensions are open for interpretation

```html
<!DOCTYPE html>
<html lang="en">
<head>
<meta charset="utf-8">
<title>KLAVO TOUR – Car Magnet</title>
<link rel="stylesheet" href="https://fonts.googleapis.com/css2?family=Anton&family=Exo+2:ital,wght@1,800&display=swap">
<style>
  :root {
    --backdrop: #b3b3b3;
    --navy: #1e2d5e;
    --red: #e52330;
    --white: #ffffff;
    --silver: #dcdbdd;
  }
  * { box-sizing: border-box; margin: 0; padding: 0; }
  html, body {
    width: 892px;
    height: 1200px;
    overflow: hidden;
    background: var(--backdrop);
  }
  .magnet {
    position: absolute;
    left: 46px;
    top: 400px;
    width: 800px;
    height: 400px;
    background: var(--navy);
    box-shadow: 2px 3px 6px rgba(0, 0, 0, 0.35);
    overflow: hidden;
  }
  .magnet__red-field {
    position: absolute;
    left: 0;
    top: 0;
    width: 200px;
    height: 100%;
    background: var(--red);
  }
  .magnet__golfer {
    position: absolute;
    left: 62px;
    top: 0;
    width: 200px;
    height: 100%;
    background: linear-gradient(90deg, #f4f4f6 0%, #ffffff 60%, #eef0f5 100%);
    border-radius: 60px 90px 0 0;
  }
  .magnet__title {
    position: absolute;
    left: 313px;
    width: 420px;
    text-align: center;
    font-family: "Anton", "Impact", sans-serif;
    color: var(--silver);
    line-height: 1;
  }
  .magnet__title--top {
    top: 16px;
    font-size: 150px;
    letter-spacing: 4px;
  }
  .magnet__title--bottom {
    top: 160px;
    font-size: 150px;
    letter-spacing: 4px;
  }
  .magnet__member-glow {
    position: absolute;
    left: 378px;
    top: 323px;
    width: 290px;
    height: 56px;
    background: radial-gradient(ellipse at center, rgba(229, 35, 48, 0.85) 0%, rgba(229, 35, 48, 0.45) 45%, rgba(229, 35, 48, 0) 75%);
  }
  .magnet__member {
    position: absolute;
    left: 313px;
    top: 327px;
    width: 420px;
    text-align: center;
    font-family: "Exo 2", sans-serif;
    font-style: italic;
    font-weight: 800;
    font-size: 34px;
    letter-spacing: 1px;
    color: var(--white);
    line-height: 1.2;
  }
</style>
</head>
<body>
  <div class="magnet">
    <div class="magnet__red-field"></div>
    <div class="magnet__golfer" role="img" aria-label="White silhouette of a golfer lining up a putt"></div>
    <div class="magnet__title magnet__title--top">KLAVO</div>
    <div class="magnet__title magnet__title--bottom">TOUR</div>
    <div class="magnet__member-glow"></div>
    <div class="magnet__member">2026 MEMBER</div>
  </div>
</body>
</html>
```